High Tech - Energy Efficiency Startup needs new look / feel for website

We are a high tech company focused on offering software, services and training courses aimed to create, design and optimize efficient Turbomachinery ( Think: Power Generation, Aerospace, Automotive, Oil & Gas, etc)

I am looking for somebody to design a new front page and 1 second level page. Then we will need to receive the photoshop files.

Here is what our website currently looks like:

www.brevolank.com

here is our work in progress which is not quite there: ua.brevolank.com << Look here for 1st and 2nd level, you will see they look different.

here is what we want it to look like in terms of look and feel and slickness...( our competitors)

www.Kortel.com
http://pqlworkshop.com

You can email questions to Desmond.Ruttle@brevolank.com
Updates

Hello All,

Several things I wanted to note / add:

1) For the Top Menu, we want to add another Item. "Industries" ( same way as Kortel has it)
2) If you find other features which you think we missed or would make sense...

Cheers,

Desmond

Reason: we have two top designs, but they are still not 100% perfect. I hope that somebody will step up and make something which will be truly amazing!

Reason: we still do not confident ending a project that's not 100% complete.

Industry/Entity Type

Training

Requirements
Must have
• If you look at our attempt to have a banner and then smaller sub squares.

The idea is that the banner moves, left to right and displayes larger version of the commercial in the little squares underneath

We need graphics for the banners. They should relate / correspond to the product / or services that is being displayed.

You can see our products and services on ua.brevolank.com so the banners should correlate.

We are really going for minimal words, good graphics, slick and sexy web 2.0 100,00o person company look and feel.

The design / designer who wins, will be given an offer to work with us afterwords and design the rest of our online properties, as well as all of our marketing material.

Please with your application submit your hourly rate for contract work.

```html
<!DOCTYPE html>
<html lang="en">
<head>
<meta charset="utf-8">
<title>Brevolank – Home</title>
<link href="https://fonts.googleapis.com/css2?family=Noto+Sans:wght@400;700&family=PT+Sans+Narrow:wght@700&display=swap" rel="stylesheet">
<style>
:root{
  --blue:#1a8ee0;
  --blue-deep:#0b3f9a;
  --blue-dark:#0c4f8f;
  --navy:#123e73;
  --title:#0d6fc0;
  --text:#1f1f1f;
  --panel:#ececec;
  --panel-hi:#f7f7f7;
  --line:#cfcfcf;
  --orange:#e8620f;
  --white:#ffffff;
  --nav-text:#2b2b2b;
}
*{box-sizing:border-box;margin:0;padding:0}
html,body{width:1167px;height:1200px;overflow:hidden;background:var(--white)}
body{position:relative;font-family:"Noto Sans",Verdana,sans-serif;color:var(--text)}
.abs{position:absolute}

/* header */
.site-header{left:0;top:0;width:1167px;height:215px}
.header-art{left:0;top:0;width:1167px;height:215px;
  background:
    linear-gradient(160deg,rgba(255,255,255,.95) 0%,rgba(226,230,236,.9) 28%,rgba(226,230,236,0) 45%),
    linear-gradient(90deg,#5fb2ee 0%,#1b8fe4 55%,#0f6fd0 100%)}
.brand{left:40px;top:78px;display:flex;align-items:center;gap:14px;color:var(--navy);font-size:50px;font-weight:700;line-height:1}
.brand-dot{width:22px;height:22px;border-radius:50%;background:var(--navy)}
.languages{right:22px;top:162px;display:flex;gap:14px}
.lang{width:39px;height:39px;border-radius:50%;border:2px solid var(--white);box-shadow:0 1px 3px rgba(0,0,0,.35)}

/* main nav */
.main-nav{left:0;top:215px;width:1167px;height:62px;background:linear-gradient(#fbfbfb,#e4e4e4);border-bottom:1px solid var(--line)}
.nav-item{position:absolute;top:0;height:62px;width:126px;text-align:center;font-size:18px;color:var(--nav-text);padding-top:14px}
.nav-item::after{content:"";position:absolute;left:50%;bottom:8px;width:86px;margin-left:-43px;height:9px;border-radius:5px;background:var(--navy)}
.nav-divider{position:absolute;top:0;width:1px;height:62px;background:#c9c9c9}

/* product tiles */
.tile{top:282px;height:228px;padding:18px 27px 22px;background:linear-gradient(#1762c9,var(--blue-deep));border:1px solid #b9c4d8}
.tile-shot{width:100%;height:100%;border:1px solid #9fb0c8}
.caption-bar{top:513px;height:54px;background:linear-gradient(var(--panel-hi),var(--panel));border:1px solid #dcdcdc;box-shadow:0 2px 2px rgba(0,0,0,.12)}
.caption-bar::before{content:"";position:absolute;left:22px;top:19px;width:17px;height:17px;border-radius:50%;background:radial-gradient(circle at 35% 35%,#3d8fe0,var(--blue-dark))}

/* feature */
.feature-banner{left:3px;top:579px;width:594px;height:227px;background:linear-gradient(100deg,#3a5fbf 0%,#7f86d6 45%,#c7b7ec 70%,#6a79c9 100%)}
.welcome{left:606px;top:579px;width:558px;height:227px;background:var(--white)}
.welcome h2{position:absolute;left:63px;top:15px;font-family:"PT Sans Narrow",sans-serif;font-weight:700;font-size:30px;color:var(--title);letter-spacing:.5px}
.welcome .bullet{position:absolute;left:27px;top:20px;width:24px;height:24px;border-radius:50%;background:radial-gradient(circle at 35% 30%,#d6f1ff,#2fa8f0 55%,#0d6fc0)}
.welcome p{position:absolute;left:31px;top:60px;width:494px;font-size:15px;line-height:22.5px;text-align:justify;hyphens:auto}
.read-more{right:24px;top:194px;font-size:17px;font-weight:700;color:var(--orange);text-decoration:underline}
.read-more::before{content:"";display:inline-block;margin-right:5px;border-left:6px solid var(--orange);border-top:4px solid transparent;border-bottom:4px solid transparent;vertical-align:2px}
.sub-bar{top:810px;height:54px;background:linear-gradient(var(--panel-hi),var(--panel));border:1px solid #dcdcdc;box-shadow:0 2px 2px rgba(0,0,0,.12)}
.sub-bar .arrow{position:absolute;left:24px;top:14px}

/* conceptual design */
.concept{left:7px;top:873px;width:1157px;height:255px;background:#f1f1f1;border:1px solid #d4d4d4;box-shadow:0 2px 3px rgba(0,0,0,.15)}
.concept h3{position:absolute;left:65px;top:12px;font-weight:400;font-size:24px;color:var(--title)}
.concept-image{position:absolute;left:32px;top:55px;width:300px;height:167px;background:linear-gradient(90deg,#3b3b3b,#9a9a9a 45%,#6a6a6a)}
.concept p{position:absolute;left:356px;top:58px;width:773px;font-size:15px;line-height:22.5px;text-align:justify;hyphens:auto}

/* footer */
.footer-nav{left:0;top:1158px;width:1167px;height:30px}
.footer-link{position:absolute;top:0;font-size:18px;color:var(--title)}
.footer-link::before{content:"";position:absolute;left:-16px;top:8px;width:3px;height:12px;border-left:2px dotted #8a8a8a;border-right:2px dotted #8a8a8a}
</style>
</head>
<body>

<header class="abs site-header">
  <div class="abs header-art" role="img" aria-label="Header artwork: turbine blades over a blue technology backdrop"></div>
  <div class="abs brand"><span class="brand-dot"></span>Brevolank</div>
  <div class="abs languages" role="group" aria-label="Languages">
    <span class="lang" style="background:#2a4a9a" title="English"></span>
    <span class="lang" style="background:linear-gradient(90deg,#2a4aa0 33%,#ffffff 33% 66%,#d8232a 66%)" title="Français"></span>
    <span class="lang" style="background:linear-gradient(#111 33%,#d8232a 33% 66%,#f5c400 66%)" title="Deutsch"></span>
    <span class="lang" style="background:#d8232a" title="中文"></span>
    <span class="lang" style="background:linear-gradient(#c8102e 25%,#f5c400 25% 75%,#c8102e 75%)" title="Español"></span>
    <span class="lang" style="background:radial-gradient(circle,#c8102e 30%,#ffffff 32%)" title="日本語"></span>
    <span class="lang" style="background:linear-gradient(90deg,#1a7a2e 40%,#d8232a 40%)" title="Português"></span>
  </div>
</header>

<nav class="abs main-nav">
  <span class="nav-item" style="left:410px">HOME</span>
  <span class="nav-divider" style="left:537px"></span>
  <span class="nav-item" style="left:538px">PRODUCTS</span>
  <span class="nav-divider" style="left:665px"></span>
  <span class="nav-item" style="left:666px">INDUSTRIES</span>
  <span class="nav-divider" style="left:793px"></span>
  <span class="nav-item" style="left:794px">CORPORATE</span>
  <span class="nav-divider" style="left:921px"></span>
  <span class="nav-item" style="left:916px">CAREERS</span>
  <span class="nav-divider" style="left:1038px"></span>
  <span class="nav-item" style="left:1039px">CONTACT</span>
</nav>

<section aria-label="Products">
  <div class="abs tile" style="left:4px;width:296px"><div class="tile-shot" role="img" aria-label="Software screenshot of a blade profile chart" style="background:linear-gradient(135deg,#f6f7fa 0%,#f6f7fa 35%,#e45a4a 55%,#f0c64a 68%,#5aa0e0 82%,#f6f7fa 95%)"></div></div>
  <div class="abs tile" style="left:304px;width:295px"><div class="tile-shot" role="img" aria-label="Software screenshot of a 3D rotor model" style="background:radial-gradient(ellipse at 45% 45%,#c9564e 0%,#8a7fc0 30%,#eef1f6 60%)"></div></div>
  <div class="abs tile" style="left:603px;width:294px"><div class="tile-shot" role="img" aria-label="Software screenshot of performance curves" style="background:linear-gradient(90deg,#f7f8fa 0%,#eef0e8 40%,#e6ece6 70%,#dfe4ea 100%)"></div></div>
  <div class="abs tile" style="left:901px;width:264px"><div class="tile-shot" role="img" aria-label="Software screenshot of a blade section view" style="background:linear-gradient(90deg,#eef2f6 0%,#9fd17a 20%,#5f8fd8 35%,#eef2f6 50%,#7fa3e0 70%,#eef2f6 85%)"></div></div>
  <div class="abs caption-bar" style="left:4px;width:296px"></div>
  <div class="abs caption-bar" style="left:304px;width:295px"></div>
  <div class="abs caption-bar" style="left:603px;width:294px"></div>
  <div class="abs caption-bar" style="left:901px;width:264px"></div>
</section>

<div class="abs feature-banner" role="img" aria-label="Innovation banner: business professional over a blue technology backdrop with the words innovation, international, process"></div>

<section class="abs welcome">
  <span class="bullet"></span>
  <h2>WELCOME</h2>
  <p>Proin sagittis feugiat pulvinar. Vivamus molestie consectetur nibh id mattis. Etiam nec tempus purus. Vivamus sagittis euismod arcu at egestas. Aenean nec turpis non tortor sollicitudin fringilla eget vel mi. Etiam egestas, justo sit amet venenatis tincidunt, nibh neque varius risus, eget dignissim neque enim in quam.</p>
  <span class="abs read-more">read more...</span>
</section>

<div class="abs sub-bar" style="left:3px;width:594px"></div>
<div class="abs sub-bar" style="left:604px;width:560px">
  <svg class="arrow" width="30" height="24" viewBox="0 0 30 24" aria-hidden="true">
    <path d="M2 12 H26 M16 3 L26 12 L16 21" fill="none" stroke="#e8620f" stroke-width="3.5" stroke-linecap="round" stroke-linejoin="round"/>
  </svg>
</div>

<section class="abs concept">
  <h3>CONCEPTUAL DESIGN</h3>
  <div class="concept-image" role="img" aria-label="Cutaway render of a jet engine"></div>
  <p>Proin sagittis feugiat pulvinar. Vivamus molestie consectetur nibh id mattis. Etiam nec tempus purus. Vivamus sagittis euismod arcu at egestas. Aenean nec turpis non tortor sollicitudin fringilla eget vel mi. Etiam egestas, justo sit amet venenatis tincidunt, nibh neque varius risus, eget dignissim neque enim in quam. Aliquam ipsum quam, porttitor eget malesuada eu, viverra sit amet urna. Etiam tristique, metus non ornare dapibus, turpis quam faucibus ante, vitae vulputate urna diam vel purus. Sed a viverra augue.</p>
</section>

<footer class="abs footer-nav">
  <span class="footer-link" style="left:420px">HOME</span>
  <span class="footer-link" style="left:520px">PRODUCTS</span>
  <span class="footer-link" style="left:650px">INDUSTRIES</span>
  <span class="footer-link" style="left:791px">CORPORATE</span>
  <span class="footer-link" style="left:933px">CAREERS</span>
  <span class="footer-link" style="left:1050px">CONTACT</span>
</footer>

</body>
</html>
```